Need DL Flyer for Real Estate Drops

We need a real estate flyer ,double sided. With content on 1 side like: Want to know what's your house is worth " contact us today and on other side agent details. We are looking for an ongoing partnership with designer so this assignment will be ongoing

```html
<!DOCTYPE html>
<html lang="en">
<head>
<meta charset="utf-8">
<title>Dunmore Real Estate – DL Flyer</title>
<link href="https://fonts.googleapis.com/css2?family=Montserrat:wght@400;500;600;700;800&display=swap" rel="stylesheet">
<style>
  :root {
    --navy: #0b1530;
    --red: #c9202a;
    --white: #ffffff;
    --backdrop: #e4e4e4;
    --photo-sky: #3f6fb8;
    --photo-wall: #d9d4cc;
    --photo-lawn: #5f8f3a;
    --photo-grey: #9a9a9a;
  }
  * { box-sizing: border-box; margin: 0; padding: 0; }
  html, body {
    width: 1138px; height: 1200px; overflow: hidden;
    background: var(--backdrop);
    font-family: "Montserrat", sans-serif;
  }
  .flyer-side {
    position: absolute; top: 62px;
    width: 502px; height: 1063px; overflow: hidden;
  }
  .flyer-side--front { left: 57px; background: var(--navy); }
  .flyer-side--back { left: 583px; background: var(--red); }
  .artwork { position: absolute; inset: 0; }

  .brand {
    position: absolute; display: flex; align-items: center; gap: 20px;
  }
  .brand__square { width: 50px; height: 50px; }
  .brand__name {
    font-family: "Montserrat", sans-serif; font-weight: 600;
    font-size: 54px; color: var(--white); letter-spacing: -0.02em; line-height: 1;
  }
  .flyer-side--front .brand { left: 70px; top: 108px; }
  .flyer-side--front .brand__square { background: var(--red); }
  .flyer-side--back .brand { left: 74px; top: 590px; }
  .flyer-side--back .brand__square { background: var(--navy); }

  .headline {
    position: absolute; left: 0; width: 100%; top: 240px;
    text-align: center; color: var(--white);
    font-weight: 800; font-size: 35px; line-height: 43px; letter-spacing: -0.035em;
  }
  .headline em { font-style: normal; color: var(--red); }

  .services {
    position: absolute; left: 50px; top: 797px;
    display: flex; align-items: center; gap: 6px;
    color: var(--white); font-size: 18px; font-weight: 500; letter-spacing: 0.08em;
  }
  .services svg { width: 20px; height: 20px; display: block; }
  .services span { margin-right: 2px; }

  .cta {
    position: absolute; left: 0; width: 100%; top: 893px; text-align: center;
    color: var(--white); font-weight: 800; font-size: 33px; letter-spacing: -0.01em;
  }
  .overleaf {
    position: absolute; left: 0; width: 100%; top: 975px; text-align: center;
    color: var(--white); font-weight: 500; font-size: 17px; letter-spacing: 0.32em;
  }

  .divider {
    position: absolute; left: 51px; top: 705px; width: 399px; height: 1px;
    background: rgba(255,255,255,0.45);
  }
  .agent-portrait {
    position: absolute; left: 0; top: 746px; width: 170px; height: 317px;
    background: linear-gradient(180deg, #b9b9b9 0%, #8c8c8c 60%, #6f6f6f 100%);
    border-top-right-radius: 70px 90px;
  }
  .agent {
    position: absolute; left: 184px; top: 748px; color: var(--white);
  }
  .agent__name { font-weight: 700; font-size: 22px; line-height: 26px; }
  .agent__role { font-weight: 600; font-size: 16.5px; line-height: 20px; margin-top: 3px; }
  .agent__company { font-weight: 400; font-size: 16.5px; line-height: 20px; }

  .contact { position: absolute; left: 183px; color: var(--white); display: flex; align-items: center; }
  .contact svg { width: 22px; height: 22px; margin-right: 8px; flex: none; }
  .contact--phone { font-weight: 700; font-size: 25px; letter-spacing: 0.01em; }
  .contact--line { font-weight: 400; font-size: 15.5px; }
  .contact--address { align-items: flex-start; line-height: 20px; }
  .contact--address svg { margin-top: 1px; }
</style>
</head>
<body>

<!-- Front side -->
<section class="flyer-side flyer-side--front">
  <svg class="artwork" viewBox="0 0 502 1063" width="502" height="1063">
    <defs>
      <linearGradient id="frontPhotoTone" x1="0" y1="0" x2="0" y2="1">
        <stop offset="0" stop-color="var(--photo-sky)"/>
        <stop offset="0.45" stop-color="var(--photo-wall)"/>
        <stop offset="0.72" stop-color="var(--photo-lawn)"/>
        <stop offset="1" stop-color="var(--photo-grey)"/>
      </linearGradient>
    </defs>
    <path class="band band--top" fill="var(--red)" d="M117,488 V447 A93,93 0 0 1 210,354 H502 V488 Z"/>
    <path class="band band--bottom" fill="var(--red)" d="M0,710 H384 V748 A95,95 0 0 1 289,843 H0 Z"/>
    <path class="photo-area" role="img" aria-label="Photo of a modern single-storey family home with a timber garage door, lawn and driveway under a blue sky"
          fill="url(#frontPhotoTone)"
          d="M0,488 H185 V486 A65,65 0 0 1 250,421 H502 V710 H384 V709 A68,68 0 0 1 316,777 H0 Z"/>
  </svg>

  <div class="brand">
    <div class="brand__square"></div>
    <div class="brand__name">dunmore</div>
  </div>

  <h1 class="headline">Want to know what's<br>your house is <em>WORTH</em>?</h1>

  <div class="services">
    <svg viewBox="0 0 20 20"><circle cx="10" cy="10" r="10" fill="#fff"/><path d="M5.5 10.3l3 3 6-6.3" fill="none" stroke="var(--red)" stroke-width="2.4" stroke-linecap="round" stroke-linejoin="round"/></svg><span>BUY</span>
    <svg viewBox="0 0 20 20"><circle cx="10" cy="10" r="10" fill="#fff"/><path d="M5.5 10.3l3 3 6-6.3" fill="none" stroke="var(--red)" stroke-width="2.4" stroke-linecap="round" stroke-linejoin="round"/></svg><span>SELL</span>
    <svg viewBox="0 0 20 20"><circle cx="10" cy="10" r="10" fill="#fff"/><path d="M5.5 10.3l3 3 6-6.3" fill="none" stroke="var(--red)" stroke-width="2.4" stroke-linecap="round" stroke-linejoin="round"/></svg><span>RENT</span>
  </div>

  <p class="cta">TALK TO US TODAY!</p>
  <p class="overleaf">SEE OVERLEAF</p>
</section>

<!-- Back side -->
<section class="flyer-side flyer-side--back">
  <svg class="artwork" viewBox="0 0 502 1063" width="502" height="1063">
    <defs>
      <linearGradient id="kitchenTone" x1="0" y1="0" x2="1" y2="1">
        <stop offset="0" stop-color="#ececec"/>
        <stop offset="0.6" stop-color="#cfcac2"/>
        <stop offset="1" stop-color="#a9a49c"/>
      </linearGradient>
      <linearGradient id="townhouseTone" x1="0" y1="0" x2="0" y2="1">
        <stop offset="0" stop-color="#8fb3d8"/>
        <stop offset="0.2" stop-color="#ddd6c8"/>
        <stop offset="0.65" stop-color="#7a6a5c"/>
        <stop offset="0.85" stop-color="var(--photo-lawn)"/>
        <stop offset="1" stop-color="#4f7d30"/>
      </linearGradient>
    </defs>
    <path class="arc arc--left" fill="var(--navy)" d="M0,0 H140 V486 H134 A134,134 0 0 1 0,352 Z"/>
    <path class="arc arc--right" fill="var(--navy)" d="M368,220 A134,134 0 0 1 502,354 V530 H368 Z"/>
    <rect class="photo-area" role="img" aria-label="Photo of a bright open-plan kitchen and living room with large windows"
          x="67" y="0" width="301" height="197" fill="url(#kitchenTone)"/>
    <path class="photo-area" role="img" aria-label="Photo of a two-storey townhouse facade with front lawn and garden"
          fill="url(#townhouseTone)"
          d="M67,204 H368 V288 A67,67 0 0 1 435,355 V530 H134 V434 A67,67 0 0 1 67,367 Z"/>
  </svg>

  <div class="brand">
    <div class="brand__square"></div>
    <div class="brand__name">dunmore</div>
  </div>

  <div class="divider"></div>

  <div class="agent-portrait" role="img" aria-label="Portrait photo of the agent in a suit"></div>

  <div class="agent">
    <p class="agent__name">Rohan MEHTA</p>
    <p class="agent__role">Managing Director/LEA</p>
    <p class="agent__company">Dunmore Real Estate</p>
  </div>

  <p class="contact contact--phone" style="top:838px">
    <svg viewBox="0 0 22 22"><circle cx="11" cy="11" r="10" fill="#fff"/><path d="M7.6 6.2c.5-.4 1.1-.3 1.4.2l.9 1.5c.3.5.2 1-.2 1.3l-.6.5c.5 1.2 1.4 2.1 2.6 2.7l.5-.6c.4-.4.9-.5 1.4-.2l1.5.9c.5.3.6.9.2 1.4l-.6.8c-.5.5-1.2.7-1.9.4-2.6-1-4.5-2.9-5.5-5.5-.3-.7-.1-1.4.4-1.9z" fill="var(--red)"/></svg>
    03 9000 1234
  </p>
  <p class="contact contact--phone" style="top:877px">
    <svg viewBox="0 0 22 22"><rect x="6" y="1.5" width="10" height="19" rx="1.8" fill="none" stroke="#fff" stroke-width="1.6"/><line x1="9.5" y1="17.5" x2="12.5" y2="17.5" stroke="#fff" stroke-width="1.4"/></svg>
    04 0000 5678
  </p>
  <p class="contact contact--line" style="top:920px">
    <svg viewBox="0 0 22 22"><rect x="2" y="5" width="18" height="12" fill="none" stroke="#fff" stroke-width="1.3"/><path d="M2 5l9 7 9-7M2 17l6.5-6M20 17l-6.5-6" fill="none" stroke="#fff" stroke-width="1.3"/></svg>
    rohan@dunmorerealestate.com.au
  </p>
  <p class="contact contact--line" style="top:954px">
    <svg viewBox="0 0 22 22"><circle cx="11" cy="11" r="9" fill="none" stroke="#fff" stroke-width="1.2"/><ellipse cx="11" cy="11" rx="4" ry="9" fill="none" stroke="#fff" stroke-width="1.2"/><path d="M2 11h18M3.5 6.5h15M3.5 15.5h15" fill="none" stroke="#fff" stroke-width="1.2"/></svg>
    www.dunmorerealestate.com.au
  </p>
  <p class="contact contact--line contact--address" style="top:989px">
    <svg viewBox="0 0 22 22"><path d="M11 1.5a7 7 0 0 0-7 7c0 5 7 12 7 12s7-7 7-12a7 7 0 0 0-7-7z" fill="#fff"/><circle cx="11" cy="8.5" r="2.6" fill="var(--red)"/></svg>
    <span>12/4 Harbour Lane,<br>Westfield 3000</span>
  </p>
</section>

</body>
</html>
```